依頼詳細
・デザイン概要
今回は、トップページデザインの募集になります。
レスポンシブデザインのサイトで、bootstrap4を利用しコーディングする予定になります。
デザイン幅は2000px、コンテンツの幅はbootstrap4デフォルトの1110pxを基準としてください。ただし最近のデザインの流行を取りいれて、フルワイドや、1200~15000px程度の幅のコンテンツをバランスよくレイアウトしてください。
コンテンツ配置は基本12分割になります。がデザインによっては、多少逸脱してもかまいません。
(12分割のコンテンツ幅については添付のPSDを参考にご覧ください)

本文のフォントはゴシック系は游ゴシック、メイリオ、明朝系は遊明朝でお願いします。
飾り文字はフリーフォントか、googleフォントを利用してください。

メイン画像部分・グローバルメニューは、ワイド適用でお願いします。

掲載画像については、基本は添付ファイルを使用してください。
また、雰囲気が合っていれば、指定外の画像を追加掲載いただいてOKです。

・その他
デザイン・ムード、参考サイトについてなど、掲載内容詳細に関しては、別添のExcel資料を参照してください。

資料上はサイト名(社名)や住所などは伏字にしております。ご提案時点ではそのまま作成をお願いします。当選確定後、本内容に修正をお願いいたします。

当選の方は、希望があれば引き続き下層ページの作成及びコーディング作業を依頼可能です。
ページ数
1ページ
希望イメージ
シンプル 複雑
単色 カラフル
暗い 明るい
日常 高級
遊び心 厳粛
未来的 伝統的
女性的 男性的
希望する色
青系
納品ファイル
• 高解像度JPG (.jpg)
• フォトショップ形式 (.psd)

クライアントと折衝しまして、norvikaplane様のデザインが一番「落ち着いてる雰囲気」と「町工場な印象」を感じたとのことで、当選とさせていただきました。

本件、多数のご提案ありがとうございました。
どの提案もとてもよく、クライアントもかなり悩んでいましたがら、最終的にムードや印象の部分でnorvikaplane様を当選とさせていいただきました。
どうもありがとうございました。
今後とも宜しくお願いいたします。

```html
<!DOCTYPE html>
<html lang="ja">
<head>
<meta charset="UTF-8">
<title>有限会社〇〇〇〇製作</title>
<link href="https://fonts.googleapis.com/css2?family=Noto+Sans+JP:wght@400;500;700&family=Roboto:wght@400;500;700&display=swap" rel="stylesheet">
<style>
:root{
  --navy:#1f4c93;
  --navy-dark:#183a73;
  --ink:#222;
  --muted:#555;
  --footer:#1b2840;
  --white:#fff;
  --line:#d6dbe3;
}
*{box-sizing:border-box;margin:0;padding:0}
html,body{width:788px;height:1200px;overflow:hidden}
body{font-family:"Noto Sans JP",sans-serif;color:var(--ink);background:#fff;position:relative}
.abs{position:absolute}
/* hero */
.hero{left:0;top:0;width:788px;height:370px;background:linear-gradient(180deg,#3f4448 0%,#5b6166 45%,#6d7276 70%,#4a4f53 100%)}
.hero::after{content:"";position:absolute;inset:0;background:linear-gradient(180deg,rgba(20,25,35,.55) 0,rgba(20,25,35,.1) 30%,rgba(20,25,35,0) 100%)}
.brand{left:22px;top:6px;color:var(--white);z-index:2}
.brand-name{font-size:19px;font-weight:700;letter-spacing:1px}
.brand-sub{font-family:"Roboto",sans-serif;font-size:8px;letter-spacing:1px;margin-top:-2px;padding-left:40px}
.top-info{right:22px;top:6px;z-index:2;color:var(--white);font-size:7px;text-align:right}
.tels{display:flex;gap:6px;margin-top:6px;justify-content:flex-end}
.tel{display:flex;align-items:center;gap:4px;background:var(--white);color:var(--navy);border-radius:11px;padding:3px 10px;font-family:"Roboto",sans-serif;font-weight:700;font-size:11px}
.tel.alt{background:var(--navy);color:var(--white)}
.gnav{left:0;top:48px;width:788px;z-index:2;display:flex;padding-left:110px;gap:0;border-top:1px solid rgba(255,255,255,.25);border-bottom:1px solid rgba(255,255,255,.25)}
.gnav a{color:var(--white);text-decoration:none;font-size:8px;padding:5px 16px;border-right:1px solid rgba(255,255,255,.3)}
/* intro band */
.intro{left:0;top:370px;width:788px;height:142px;background:var(--navy);color:var(--white);text-align:center;overflow:hidden}
.intro-bg{position:absolute;left:0;right:0;top:40px;font-family:"Roboto",sans-serif;font-weight:700;font-size:70px;color:rgba(255,255,255,.05);white-space:nowrap}
.intro p{position:relative;font-size:9px;line-height:1.9;padding-top:44px}
.intro .accent{color:#8fb3ea}
/* sections */
.heading{display:flex;align-items:flex-start;gap:8px}
.heading::before{content:"";width:4px;height:30px;background:var(--navy);margin-top:2px}
.heading h2{font-size:20px;font-weight:500;line-height:1.1}
.heading span{display:block;font-family:"Roboto",sans-serif;font-size:7px;color:var(--muted);margin-top:2px}
.lead{color:var(--navy);font-size:11px;font-weight:700;margin:12px 0 8px}
.body-text{font-size:8px;line-height:1.9;color:var(--muted)}
.more{display:inline-flex;align-items:center;justify-content:space-between;width:96px;height:22px;background:var(--navy);color:var(--white);font-family:"Roboto",sans-serif;font-size:9px;padding:0 10px;margin-top:12px}
.photo{background:linear-gradient(135deg,#8c9196,#d3d6d9 45%,#6f7479)}
.tech-text{left:58px;top:552px;width:260px}
.tech-photo{left:352px;top:524px;width:436px;height:180px}
.prod-photo{left:0;top:776px;width:420px;height:170px;background:linear-gradient(135deg,#a7adb3,#e6e8ea 40%,#7c8288)}
.prod-text{left:470px;top:800px;width:280px}
/* company */
.company{left:0;top:946px;width:394px;height:170px;background:linear-gradient(135deg,#1c2330,#3a4350 60%,#20262f);color:var(--white);padding:22px 0 0 60px}
.company .heading::before{background:var(--white)}
.company .heading span{color:#cfd6e0}
.company .body-text{color:#e4e8ee;margin-top:10px}
.more.light{background:var(--white);color:var(--navy)}
.map{left:394px;top:946px;width:394px;height:170px;background:linear-gradient(160deg,#eef0ec,#f6e9e3 50%,#e6ecf3)}
.to-top{left:610px;top:1100px;width:26px;height:26px;border-radius:50%;background:var(--navy);z-index:3;display:flex;align-items:center;justify-content:center}
/* footer */
.footer{left:0;top:1116px;width:788px;height:84px;background:var(--footer);color:var(--white)}
.f-brand{left:36px;top:14px}
.f-brand .brand-name{font-size:15px}
.f-brand .brand-sub{font-size:7px;padding-left:30px}
.f-addr{left:36px;top:52px;font-size:7px;line-height:1.6;color:#c5cdd9}
.f-nav{right:36px;top:24px;display:flex;gap:12px;font-size:7px}
.f-copy{right:36px;top:60px;font-family:"Roboto",sans-serif;font-size:6px;color:#9aa5b5}
</style>
</head>
<body>
<div class="abs hero" role="img" aria-label="工場内の機械設備の写真"></div>
<div class="abs brand"><div class="brand-name">有限会社〇〇〇〇製作</div><div class="brand-sub">Kestrel Spring Works</div></div>
<div class="abs top-info">
  <div>お気軽にお問い合わせください 受付時間 8:00〜17:00</div>
  <div class="tels">
    <div class="tel"><svg width="9" height="9" viewBox="0 0 24 24"><path fill="currentColor" d="M6.6 10.8a15 15 0 006.6 6.6l2.2-2.2a1 1 0 011-.3 11 11 0 003.6.6 1 1 0 011 1V20a1 1 0 01-1 1A17 17 0 013 4a1 1 0 011-1h3.5a1 1 0 011 1 11 11 0 00.6 3.6 1 1 0 01-.3 1z"/></svg>012-987-6543</div>
    <div class="tel alt"><svg width="9" height="9" viewBox="0 0 24 24"><path fill="currentColor" d="M6.6 10.8a15 15 0 006.6 6.6l2.2-2.2a1 1 0 011-.3 11 11 0 003.6.6 1 1 0 011 1V20a1 1 0 01-1 1A17 17 0 013 4a1 1 0 011-1h3.5a1 1 0 011 1 11 11 0 00.6 3.6 1 1 0 01-.3 1z"/></svg>012-987-6543</div>
  </div>
</div>
<nav class="abs gnav"><a>トップ</a><a>会社案内</a><a>技術紹介</a><a>製品紹介</a><a>採用情報</a></nav>

<section class="abs intro">
  <div class="intro-bg">Kestrel Spring Works</div>
  <p><span class="accent">〇〇〇〇</span>製作所は、昔ながらの町工場として精密ばねの製造・販売を行っています。<br>圧縮ばね、引張ばね、ねじりばね、線細工品など、小ロットから量産まで幅広く対応いたします。<br>長年の経験と確かな技術で、お客様のご要望にお応えします。</p>
</section>

<section class="abs tech-text">
  <div class="heading"><div><h2>技術紹介</h2><span>Technology</span></div></div>
  <p class="lead">納得の設計と高い技術力</p>
  <p class="body-text">熟練の職人が一つひとつ丁寧に仕上げます。<br>試作から量産まで一貫して対応いたします。<br>図面がなくてもお気軽にご相談ください。</p>
  <a class="more">More <span>›</span></a>
</section>
<div class="abs tech-photo photo" role="img" aria-label="ばね加工機械の写真"></div>

<div class="abs prod-photo" role="img" aria-label="金属ばね製品の写真"></div>
<section class="abs prod-text">
  <div class="heading"><div><h2>製品紹介</h2><span>Products</span></div></div>
  <p class="lead">高精度・高品質な製品加工</p>
  <p class="body-text">用途に合わせた多彩な製品をご用意しています。<br>材質や形状のご指定にも柔軟に対応します。</p>
  <a class="more">More <span>›</span></a>
</section>

<section class="abs company" role="img" aria-label="ばねの写真を背景にした会社案内">
  <div class="heading"><div><h2>会社案内</h2><span>Company</span></div></div>
  <p class="body-text">地域に根ざした町工場として<br>確かなものづくりを続けています。</p>
  <a class="more light">More <span>›</span></a>
</section>
<div class="abs map" role="img" aria-label="会社周辺の地図"></div>
<div class="abs to-top"><svg width="10" height="10" viewBox="0 0 10 10"><path d="M2 6.5L5 3.5 8 6.5" stroke="#fff" stroke-width="1.4" fill="none"/></svg></div>

<footer class="abs footer">
  <div class="abs f-brand"><div class="brand-name">有限会社〇〇〇〇製作</div><div class="brand-sub">Kestrel Spring Works</div></div>
  <div class="abs f-addr">〒000-0000 〇〇県〇〇市〇〇町1-2-3<br>TEL 012-987-6543 / FAX 012-987-6544</div>
  <nav class="abs f-nav"><span>トップ</span><span>会社案内</span><span>技術紹介</span><span>製品紹介</span><span>採用情報</span></nav>
  <div class="abs f-copy">© 2024 KESTREL SPRING WORKS</div>
</footer>
</body>
</html>
```